Security based company delivering High Risk Training to Law Enforcement Agencies Worldwide.

We need a Web design for a company doing business in Washington D.C. We deliver High Risk Training to Law Enforcement Agencies throughout the world. Our focus is on Improvised Explosive Devices. We train Bomb Technicians and First Responders in all aspects relating to bombings and criminal incidents globally.
Updates

Reason: We have uploaded our logo. Thank you.

Target Market(s)

Military and Law Enforcement Personnel from around the world.

Industry/Entity Type

Business

Requirements
Should not have
• Do not include cartoon like characters.

```html
<!DOCTYPE html>
<html lang="en">
<head>
<meta charset="utf-8">
<title>High Risk Training</title>
<link href="https://fonts.googleapis.com/css2?family=Open+Sans:wght@300;400;600;700&display=swap" rel="stylesheet">
<style>
:root{
  --orange:#f26522;
  --ink:#333333;
  --muted:#777777;
  --dark:#1b1b1b;
  --darker:#141414;
  --footer:#262626;
  --line:#3a3a3a;
  --light:#f2f2f2;
  --white:#ffffff;
}
*{margin:0;padding:0;box-sizing:border-box}
html,body{width:1200px;height:3120px;overflow:hidden}
body{font-family:"Open Sans",Arial,sans-serif;color:var(--ink);background:var(--white);position:relative}
.abs{position:absolute}

/* header */
.site-header{position:absolute;left:0;top:0;width:1200px;height:208px;background:var(--white)}
.brand{position:absolute;left:84px;top:74px;font-size:64px;font-weight:400;color:var(--orange);line-height:1}
.header-phone{position:absolute;right:84px;top:64px;font-size:26px;font-weight:600;color:var(--ink);display:flex;align-items:center;gap:12px}
.search{position:absolute;right:84px;top:124px;width:240px;height:38px;background:#2b2b2b;color:#999;font-size:15px;padding:8px 14px;display:flex;justify-content:space-between;align-items:center}
.main-nav{position:absolute;left:0;top:208px;width:1200px;height:52px;background:#222}
.main-nav ul{list-style:none;display:flex;margin-left:84px;height:52px}
.main-nav li{padding:0 26px;line-height:52px;font-size:17px;font-weight:600;color:var(--white);border-right:1px solid #333}
.main-nav li.active{background:var(--orange)}

/* hero */
.hero{position:absolute;left:0;top:260px;width:1200px;height:500px;background:linear-gradient(180deg,#b9b4a8 0%,#d8d2c4 45%,#8f8a74 75%,#6e6b58 100%)}
.slider-arrow{position:absolute;top:214px;width:60px;height:60px;border-radius:50%;background:rgba(0,0,0,.45)}

/* services */
.services{position:absolute;left:0;top:760px;width:1200px;height:540px;background:linear-gradient(180deg,#222 0%,#141414 100%);color:#bbb;text-align:center}
.section-title{font-size:34px;font-weight:400;letter-spacing:1px}
.services .section-title{position:absolute;top:60px;width:100%;color:#d9a05b}
.services .intro{position:absolute;left:100px;width:1000px;top:126px;font-size:15px;line-height:24px;color:#999}
.divider{position:absolute;height:2px;background:#888}
.service{position:absolute;top:220px;width:300px;text-align:center}
.service .icon{width:100px;height:100px;border-radius:50%;border:2px solid #444;margin:0 auto;display:flex;align-items:center;justify-content:center}
.service h3{font-size:26px;font-weight:400;margin-top:22px;color:#888}
.service.is-active h3{color:var(--white)}
.service p{font-size:15px;line-height:23px;margin-top:10px;color:#bbb}

/* welcome */
.welcome{position:absolute;left:0;top:1300px;width:1200px;height:428px;background:var(--white)}
.welcome .portrait{position:absolute;left:170px;top:60px;width:200px;height:340px;background:linear-gradient(180deg,#c9b89a 0%,#8c7a5c 55%,#5d5040 100%)}
.welcome h2{position:absolute;left:448px;top:80px;font-size:38px;font-weight:400;color:var(--ink)}
.welcome .body{position:absolute;left:448px;top:162px;width:660px;font-size:15px;line-height:24px;color:var(--muted)}
.btn{display:inline-block;border:2px solid #555;padding:6px 14px;font-size:14px;font-weight:600;letter-spacing:.5px}
.welcome .btn{position:absolute;left:448px;top:340px;color:var(--ink)}

/* training band */
.training{position:absolute;left:0;top:1728px;width:1200px;height:512px;background:linear-gradient(180deg,#5a5650 0%,#3b3936 45%,#4a3f34 75%,#2c2a27 100%);color:var(--white);text-align:center}
.training h2{position:absolute;top:70px;width:100%;font-size:38px;font-weight:400}
.training .headline{position:absolute;left:60px;width:1080px;top:176px;font-size:30px;line-height:44px;font-weight:400;white-space:nowrap}
.training .body{position:absolute;left:100px;width:1000px;top:290px;font-size:15px;line-height:24px;color:#ddd}
.training .btn{position:absolute;left:542px;top:406px;color:var(--white);border-color:#ddd}

/* enquiry */
.enquiry{position:absolute;left:0;top:2240px;width:1200px;height:520px;background:linear-gradient(180deg,#ffffff 0%,#eeeeee 100%)}
.enquiry h2{position:absolute;top:62px;width:100%;text-align:center;font-size:38px;font-weight:400;color:var(--ink)}
.field{position:absolute;height:48px;background:var(--white);border:1px solid #ccc;font-size:16px;color:#555;padding:12px 16px}
.send{position:absolute;left:536px;top:400px;width:112px;height:48px;background:#2b2b2b;color:var(--white);font-size:18px;font-weight:600;text-align:center;line-height:48px}

/* footer */
.site-footer{position:absolute;left:0;top:2760px;width:1200px;height:360px;background:var(--footer);color:#bbb}
.site-footer h4{font-size:24px;font-weight:400;color:var(--white)}
.footer-col{position:absolute;top:36px}
.quote{font-size:15px;line-height:23px;color:#aaa;font-style:italic;margin-top:28px;width:380px;padding-left:20px}
.quote-by{text-align:right;color:var(--white);font-size:15px;margin-top:18px;width:400px}
.contact-list{list-style:none;margin-top:24px}
.contact-list li{display:flex;align-items:flex-start;gap:16px;font-size:15px;line-height:22px;margin-bottom:12px}
.contact-list svg{flex:none;margin-top:3px}
.follow p{font-size:15px;line-height:23px;width:320px;margin-top:24px;color:#aaa}
.socials{display:flex;gap:18px;margin-top:26px}
.socials span{width:44px;height:44px;border-radius:50%;border:2px solid #777}
.copyright{position:absolute;left:84px;bottom:24px;font-size:14px;color:#888}
</style>
</head>
<body>

<header class="site-header">
  <div class="brand">Logo</div>
  <div class="header-phone">+1 202 555 0148
    <svg width="26" height="26" viewBox="0 0 24 24"><path d="M6.6 10.8a15 15 0 0 0 6.6 6.6l2.2-2.2c.3-.3.7-.4 1-.2 1.1.4 2.3.6 3.6.6.6 0 1 .4 1 1V20c0 .6-.4 1-1 1A17 17 0 0 1 3 4c0-.6.4-1 1-1h3.5c.6 0 1 .4 1 1 0 1.3.2 2.5.6 3.6.1.3 0 .7-.2 1z" fill="#333"/></svg>
  </div>
  <div class="search"><span>Search</span>
    <svg width="16" height="16" viewBox="0 0 16 16"><circle cx="6.5" cy="6.5" r="5" fill="none" stroke="#aaa" stroke-width="2"/><path d="M10.5 10.5L15 15" stroke="#aaa" stroke-width="2"/></svg>
  </div>
</header>

<nav class="main-nav">
  <ul>
    <li class="active">HOME</li>
    <li>ABOUT US</li>
    <li>SERVICES</li>
    <li>TRAININGS</li>
    <li>TESTIMONIALS</li>
    <li>BLOG</li>
    <li>CONTACT US</li>
  </ul>
</nav>

<section class="hero" role="img" aria-label="Photo of a bomb technician in a protective suit handling a device near a stop sign">
  <div class="slider-arrow" style="right:24px">
    <svg width="60" height="60" viewBox="0 0 60 60"><path d="M26 20l10 10-10 10" fill="none" stroke="#fff" stroke-width="3"/></svg>
  </div>
</section>

<section class="services">
  <h2 class="section-title">OUR SERVICES</h2>
  <div class="divider" style="left:556px;top:110px;width:88px;background:#555"></div>
  <p class="intro">We prepare bomb technicians and first responders for the hardest calls. Our instructors bring field experience from agencies worldwide, and every course is built around real incidents, modern devices and safe procedures.</p>

  <div class="service is-active" style="left:120px">
    <div class="icon">
      <svg width="44" height="44" viewBox="0 0 44 44"><circle cx="22" cy="22" r="12" fill="none" stroke="#ddd" stroke-width="5" stroke-dasharray="5 4"/><circle cx="22" cy="22" r="5" fill="#ddd"/></svg>
    </div>
    <h3>High Risk Training</h3>
    <p>Hands-on courses for tactical teams<br>facing live threats in the field<br>under real time pressure.</p>
  </div>

  <div class="service" style="left:450px">
    <div class="icon">
      <svg width="50" height="36" viewBox="0 0 50 36"><rect x="14" y="6" width="18" height="10" rx="2" fill="#666"/><rect x="30" y="9" width="18" height="3" fill="#666"/><rect x="4" y="16" width="40" height="10" rx="3" fill="#666"/><rect x="2" y="26" width="44" height="6" rx="3" fill="#555"/></svg>
    </div>
    <h3>Explosive Devices</h3>
    <p>Study of improvised devices,<br>their components and safe<br>handling on every scene.</p>
  </div>

  <div class="service" style="left:780px">
    <div class="icon">
      <svg width="44" height="44" viewBox="0 0 44 44"><circle cx="20" cy="26" r="13" fill="#666"/><rect x="26" y="10" width="6" height="6" fill="#666"/><path d="M32 11q5-6 9-2" fill="none" stroke="#888" stroke-width="2"/></svg>
    </div>
    <h3>Bomb Technicians</h3>
    <p>Certification tracks for bomb<br>squads and responders working<br>in agencies around the world.</p>
  </div>
</section>

<section class="welcome">
  <div class="portrait" role="img" aria-label="Photo of a soldier in camouflage uniform with arms crossed"></div>
  <h2>WELCOME TO OUR SITE</h2>
  <div class="divider" style="left:448px;top:140px;width:300px;background:#333"></div>
  <div class="divider" style="left:800px;top:140px;width:300px;background:#333"></div>
  <svg class="abs" style="left:764px;top:133px" width="16" height="16"><circle cx="8" cy="8" r="6" fill="#333"/></svg>
  <div class="body">
    <p>Our team trains law enforcement and military personnel in every aspect of bombing incidents. Courses cover threat recognition, device disruption, post blast investigation and scene safety, taught by instructors who have worked these cases across many countries.</p>
    <p style="margin-top:12px">We build each program around the needs of the agency, from first responders to senior bomb technicians preparing for complex operations.</p>
  </div>
  <span class="btn">READ MORE</span>
</section>

<section class="training" role="img" aria-label="Background photo of a vehicle explosion during a training exercise">
  <h2>HIGH RISK TRAINING</h2>
  <div class="divider" style="left:400px;top:136px;width:180px;background:#ddd"></div>
  <div class="divider" style="left:620px;top:136px;width:180px;background:#ddd"></div>
  <svg class="abs" style="left:592px;top:129px" width="16" height="16"><circle cx="8" cy="8" r="6" fill="#fff"/></svg>
  <p class="headline">MIRUM EST NOTARE QUAM LITTERA GOTHICA, QUAM NUNC<br>PUTAMUS PARUM CLARAM, ANTEPOSUERIT.</p>
  <p class="body">Our field exercises recreate the conditions teams meet on real calls. Trainees work through staged vehicle incidents, suspect packages and post blast scenes with close guidance, learning to stay calm, move with purpose and protect the public and each other.</p>
  <span class="btn">READ MORE</span>
</section>

<section class="enquiry">
  <h2>QUICK ENQUIRY</h2>
  <div class="divider" style="left:420px;top:122px;width:160px;background:#333"></div>
  <div class="divider" style="left:620px;top:122px;width:160px;background:#333"></div>
  <svg class="abs" style="left:592px;top:115px" width="16" height="16"><circle cx="8" cy="8" r="6" fill="#333"/></svg>
  <div class="field" style="left:120px;top:184px;width:440px">Name</div>
  <div class="field" style="left:120px;top:252px;width:440px">Email</div>
  <div class="field" style="left:120px;top:320px;width:440px">Phone</div>
  <div class="field" style="left:632px;top:184px;width:440px;height:184px">Send your message</div>
  <div class="send">SEND</div>
</section>

<footer class="site-footer">
  <div class="footer-col" style="left:84px">
    <h4>Testimonials</h4>
    <p class="quote">&ldquo;The course gave our unit the confidence to handle suspect devices safely. The instructors were clear, patient and knew the work first hand.&rdquo;</p>
    <p class="quote-by">&mdash; Mark Ellison</p>
  </div>
  <div class="footer-col" style="left:540px">
    <h4>Contact</h4>
    <ul class="contact-list">
      <li><svg width="16" height="20" viewBox="0 0 16 20"><path d="M8 0a7 7 0 0 0-7 7c0 5 7 13 7 13s7-8 7-13a7 7 0 0 0-7-7z" fill="#bbb"/><circle cx="8" cy="7" r="2.5" fill="#262626"/></svg><span>1420 Harbor Point Ave.<br>Arlington VA 22201</span></li>
      <li><svg width="18" height="14" viewBox="0 0 18 14"><rect width="18" height="14" rx="2" fill="#bbb"/><path d="M1 2l8 6 8-6" fill="none" stroke="#262626" stroke-width="1.5"/></svg><span>info@fieldreadyacademy.com</span></li>
      <li><svg width="16" height="16" viewBox="0 0 24 24"><path d="M6.6 10.8a15 15 0 0 0 6.6 6.6l2.2-2.2c.3-.3.7-.4 1-.2 1.1.4 2.3.6 3.6.6.6 0 1 .4 1 1V20c0 .6-.4 1-1 1A17 17 0 0 1 3 4c0-.6.4-1 1-1h3.5c.6 0 1 .4 1 1 0 1.3.2 2.5.6 3.6.1.3 0 .7-.2 1z" fill="#bbb"/></svg><span>+1 202 555 0148</span></li>
    </ul>
  </div>
  <div class="footer-col follow" style="left:836px">
    <h4>Follow Us</h4>
    <p>Follow us through our social network and get connected with our updates.</p>
    <div class="socials"><span></span><span></span><span></span><span></span></div>
  </div>
  <p class="copyright">Copyright &copy;2015. All Rights Reserved</p>
</footer>

</body>
</html>
```